New Real Estate business seek modern cutting edge stationery Design for Letterhead,Presentation fold

We need full stationary designs for new real estate company from Toronto Ontario. We would like a very cool, new, sleek, modern cutting edge design design for email signature, letterhead, envelope and presentation folder.

Let your imagination run wild, looking for a really cool package

Attached is all versions of my logo, the main colours are Red,white and black.

Industry/Entity Type

Real Estate

Requirements
Must have
• Envelope must have a Top secret stamp water marked into the middle
• Presentation folder must have SOLD sign inside
• Follow logo colour seem .
• make all txt editable

```html
<!DOCTYPE html>
<html lang="en">
<head>
<meta charset="utf-8">
<title>Hearthlane Realty — Presentation Folder</title>
<link href="https://fonts.googleapis.com/css2?family=Didact+Gothic&display=swap" rel="stylesheet">
<style>
  :root {
    --brand-red: #ed1c24;
    --label-red: #b8141a;
    --fold-line: #f7777b;
    --white: #ffffff;
    --black: #000000;
  }
  html, body {
    margin: 0;
    padding: 0;
    overflow: hidden;
    background: var(--brand-red);
  }
  .folder {
    position: relative;
    width: 1200px;
    height: 822px;
    background: var(--brand-red);
    font-family: "Didact Gothic", "Century Gothic", sans-serif;
    overflow: hidden;
  }
  .panel-label {
    position: absolute;
    top: 15px;
    margin: 0;
    font-size: 19px;
    font-weight: 400;
    line-height: 24px;
    letter-spacing: 12px;
    color: var(--label-red);
  }
  .panel-label--back { left: 232px; }
  .panel-label--front { left: 881px; }
  .fold-line {
    position: absolute;
    left: 599px;
    top: 0;
    height: 822px;
    border-left: 2px dashed var(--fold-line);
    opacity: 0.8;
  }
  .front-block {
    position: absolute;
    left: 1040px;
    top: 258px;
    width: 160px;
    height: 262px;
    background: var(--white);
  }
  .front-wordmark {
    position: absolute;
    right: 180px;
    top: 258px;
    height: 262px;
    margin: 0;
    display: flex;
    flex-direction: column;
    justify-content: center;
    align-items: flex-end;
    color: var(--white);
    font-weight: 400;
    text-align: right;
  }
  .front-wordmark__line {
    font-size: 82px;
    line-height: 0.92;
  }
  .front-wordmark__sub {
    margin-top: 14px;
    font-size: 20px;
    line-height: 1;
    letter-spacing: 10px;
    margin-right: -10px;
  }
  .contact {
    position: absolute;
    left: 29px;
    top: 757px;
    margin: 0;
    font-size: 11.2px;
    line-height: 13px;
    color: var(--white);
  }
  .brand-plate {
    position: absolute;
    left: 501px;
    top: 726px;
    width: 288px;
    height: 96px;
    background: var(--black);
    color: var(--white);
    display: flex;
    align-items: center;
  }
  .brand-plate__square {
    width: 72px;
    height: 72px;
    margin: 0 14px 0 12px;
    background: var(--white);
    flex: none;
  }
  .brand-plate__name {
    margin: 0;
    font-size: 30px;
    line-height: 1;
  }
  .brand-plate__tagline {
    margin: 8px 0 0;
    font-size: 7.5px;
  }
</style>
</head>
<body>
  <main class="folder">
    <h2 class="panel-label panel-label--back">BACK</h2>
    <h2 class="panel-label panel-label--front">FRONT</h2>
    <div class="fold-line"></div>

    <div class="front-block"></div>
    <h1 class="front-wordmark">
      <span class="front-wordmark__line">Hearth</span>
      <span class="front-wordmark__line">lane</span>
      <span class="front-wordmark__sub">REALTY</span>
    </h1>

    <p class="contact">
      Address: Lorem ipsum dolor sit amet, Aliquam elementum fermentum elit,<br>
      Eget eleifend ipsum sollicitudin at. 19088<br>
      Tel No: 123.456.778 &nbsp;| &nbsp;Fax No: 123.456.778 &nbsp;| &nbsp;Email: email@email.com
    </p>

    <div class="brand-plate">
      <div class="brand-plate__square"></div>
      <div>
        <p class="brand-plate__name">Hearthlane<br>Realty</p>
        <p class="brand-plate__tagline">Your one stop shop for everything. Real Estate</p>
      </div>
    </div>
  </main>
</body>
</html>
```